Buchcover-Design für Coaching-Buch
Zielgruppe
22 Coaches (m/w/d) haben zusammen ein Buch geschrieben - mit ihren besten Tipps, Mut machenden Geschichten und Inspirationen. Herausgekommen ist 'Die stille Mentorin am Fensterbrett - 22 Schatzkisten lüften ihre Rätsel'. Zielgruppe sind vorwiegend Frauen, häufig mit spirituellem Hintergrund oder an Selbstentwicklung interessiert, sowie Menschen, die sich ermutigen lassen möchten und Menschen, die inspirierende Texte und Geschichten mögen. Die Themen sind ganz unterschiedlich, von Selbstliebe über die Wirkung von Farben, vom Überwinden von Krisen und Angst, Umgang mit Emotionen etc. pp. - ein ganzer Blumenstrauß an Themen.
Aufgabenstellung
Der Titel 'Die stille Mentorin am Fensterbrett' kam auf, weil wir die Vorstellung hatten, dass in dem Buch vielleicht abends im Bett gelesen wird und man dann ruhig schlafen kann.
Warum Füllhörner? Nun, jeder Coach hat viel zu geben. Zu jedem Text wird es ein Geschenk geben, das die Autor*innen online zur Verfügung stellen. Dies sind PDFs mit Tipps, Meditationen oder sogar eine kurze Gratis-Session. Es braucht also etwas auf dem Cover, das darauf hindeutet, vielleicht eine Plakette oder etwas Ähnliches, das 'Mit 22 Geschenken' besagt. Im Buchsatz wird dies durch einen Link (E-Book) und durch einen QR-Code (Print) umgesetzt.

```html
<!DOCTYPE html>
<html lang="de">
<head>
<meta charset="utf-8">
<title>Die stille Mentorin am Fensterbrett – Buchcover</title>
<link rel="stylesheet" href="https://fonts.googleapis.com/css2?family=Questrial&family=Lato:wght@400&display=swap">
<style>
  :root {
    --stage: #e6e6e4;
    --paper: #ffffff;
    --title-red: #c8161d;
    --subtitle-red: #d0124a;
    --badge-red: #cc1419;
    --art-deep: #c0204e;
    --art-mid: #dc5a7e;
    --art-soft: #f4c6d2;
  }
  * { margin: 0; padding: 0; box-sizing: border-box; }
  html, body {
    width: 1169px;
    height: 1200px;
    overflow: hidden;
    background: var(--stage);
  }
  .canvas {
    position: relative;
    width: 1169px;
    height: 1200px;
  }
  .cover {
    position: absolute;
    left: 209px;
    top: 50px;
    width: 751px;
    height: 1100px;
    background: var(--paper);
    overflow: hidden;
  }
  .cover-art {
    position: absolute;
    left: 0;
    top: 174px;
    width: 510px;
    height: 926px;
  }
  .title {
    position: absolute;
    right: 65px;
    top: 104px;
    font-family: "Questrial", sans-serif;
    font-weight: 400;
    font-size: 60px;
    line-height: 65px;
    color: var(--title-red);
    text-align: right;
    letter-spacing: 0.5px;
  }
  .subtitle {
    position: absolute;
    right: 65px;
    top: 532px;
    font-family: "Lato", sans-serif;
    font-size: 18px;
    line-height: 25px;
    color: var(--subtitle-red);
    text-align: right;
    text-transform: uppercase;
    letter-spacing: 0.3px;
  }
  .gift-badge {
    position: absolute;
    left: 504px;
    top: 934px;
    width: 280px;
    height: 38px;
    background: var(--badge-red);
    transform: rotate(-6deg);
    transform-origin: left bottom;
    font-family: "Lato", sans-serif;
    font-size: 18px;
    line-height: 38px;
    color: var(--paper);
    padding-left: 18px;
    text-transform: uppercase;
    letter-spacing: 0.3px;
  }
</style>
</head>
<body>
<div class="canvas">
  <div class="cover">
    <svg class="cover-art" role="img" aria-label="Platz für das Aquarell-Porträtmotiv in Rot- und Rosatönen" viewBox="0 0 510 926" preserveAspectRatio="none" xmlns="http://www.w3.org/2000/svg">
      <defs>
        <radialGradient id="artTone" cx="0.2" cy="0.65" r="0.85">
          <stop offset="0" stop-color="var(--art-deep)"/>
          <stop offset="0.45" stop-color="var(--art-mid)"/>
          <stop offset="0.8" stop-color="var(--art-soft)"/>
          <stop offset="1" stop-color="var(--paper)" stop-opacity="0"/>
        </radialGradient>
      </defs>
      <rect x="0" y="0" width="510" height="926" fill="url(#artTone)"/>
    </svg>

    <h1 class="title">Die<br>stille<br>Mentorin<br>am<br>Fenster-<br>brett</h1>

    <p class="subtitle">22 Schatzkisten<br>lüften ihre<br>Rätsel.</p>

    <div class="gift-badge">Mit 22 Geschenken</div>
  </div>
</div>
</body>
</html>
```